Business Cards

Hi,
We are due for an update of bussiness cards. I Hvae also included jpg of our current card with old logo just so you can see why we want change). We do have a current logo (attached) however would like the cards to be more modern and edgy, double sided, with the following words (final to be provided in suitable format for printer):
Below are some of the essentials;

FRONT

KRPVN logo
Learn to Dance
Modern Jive and West Coast Swing
0417 862 551

BACK

Dance, it’s cheaper than therapy!
New Dancers – FREE Entry

```html
<!DOCTYPE html>
<html lang="en">
<head>
<meta charset="utf-8">
<title>KRPVN Business Cards</title>
<link rel="stylesheet" href="https://fonts.googleapis.com/css2?family=Kaushan+Script&family=Roboto:wght@400&display=swap">
<style>
  :root {
    --backdrop: #e4e6ea;
    --card-black: #0b0b0c;
    --brand-orange: #f08a1c;
    --orange-light: #f7a12c;
    --orange-deep: #ec741a;
    --white: #ffffff;
    --muted-white: #e9e9e9;
  }
  * { margin: 0; padding: 0; box-sizing: border-box; }
  html, body {
    width: 1200px;
    height: 900px;
    overflow: hidden;
    background: var(--backdrop);
  }
  .canvas {
    position: relative;
    width: 1200px;
    height: 900px;
    display: flex;
    flex-direction: column;
    align-items: center;
    justify-content: center;
    gap: 60px;
  }
  .card {
    position: relative;
    width: 630px;
    height: 360px;
    border-radius: 4px;
    overflow: hidden;
    box-shadow: 0 10px 28px rgba(0,0,0,0.18);
  }

  /* Front side */
  .card-front { background: var(--card-black); }
  .dancers-art {
    position: absolute;
    left: 60px;
    top: 40px;
    width: 250px;
    height: 150px;
    display: block;
  }
  .tagline {
    position: absolute;
    left: 70px;
    top: 210px;
    font-family: "Kaushan Script", cursive;
    font-size: 26px;
    color: var(--brand-orange);
  }
  .brand-name {
    position: absolute;
    right: 70px;
    top: 150px;
    font-family: "Kaushan Script", cursive;
    font-size: 54px;
    line-height: 1;
    color: var(--brand-orange);
  }
  .contact-block {
    position: absolute;
    right: 70px;
    top: 235px;
    text-align: center;
    font-family: "Roboto", sans-serif;
    font-size: 17px;
    line-height: 1.55;
    color: var(--muted-white);
  }

  /* Back side */
  .card-back {
    background: linear-gradient(135deg, var(--orange-deep) 0%, var(--orange-light) 55%, var(--orange-deep) 100%);
    display: flex;
    flex-direction: column;
    align-items: center;
    justify-content: center;
    gap: 6px;
  }
  .back-line {
    font-family: "Kaushan Script", cursive;
    font-size: 30px;
    color: var(--white);
    text-align: center;
  }
</style>
</head>
<body>
<main class="canvas">
  <section class="card card-front">
    <svg class="dancers-art" viewBox="0 0 250 150" role="img" aria-label="Illustration of three leaping dancer silhouettes in white and orange">
      <defs>
        <linearGradient id="dancersTone" x1="0" y1="0" x2="1" y2="1">
          <stop offset="0" stop-color="#3a3a3a"/>
          <stop offset="0.5" stop-color="#8a5a2a"/>
          <stop offset="1" stop-color="#3a3a3a"/>
        </linearGradient>
      </defs>
      <rect width="250" height="150" rx="6" fill="url(#dancersTone)"/>
    </svg>
    <p class="tagline">Learn To Dance</p>
    <h1 class="brand-name">KRPVN</h1>
    <div class="contact-block">
      <p class="styles">Modern Jive and West Coast Swing</p>
      <p class="web">www.krpvndance.com.au</p>
      <p class="phone">0417 862 551</p>
    </div>
  </section>

  <section class="card card-back">
    <p class="back-line">Dance, It's Cheaper Than Therapy!</p>
    <p class="back-line">New Dancer's – Free Entry</p>
  </section>
</main>
</body>
</html>
```